Product Designer Business Card

Small product design, engineering and prototyping firm in need of a clean, professional business card design. To support our 3D design and drawing services, we offer 3D printing, molding, and casting of plastics, silicones, resins, etc. Our logo can still be modified/changed if necessary. The red/orange color is preferred, but may be substituted with blue or green, potentially. Either way, the colour of the logo should be match/compliment colors used throughout the design. One thought is to have the logo/contact info on one side, with the other side describing services offered, like with a small icon of 3D printer, molding, casting, and computer with a 3D model on-screen.
Industry/Entity Type
Mechanical Engineering
Contact Information for Business Card
Company: Halvick Design
Phone: 613-582-4179
Email: myles@halvickdesign.ca

```html
<!DOCTYPE html>
<html lang="en">
<head>
<meta charset="utf-8">
<title>Halvick Design — Business Card</title>
<link href="https://fonts.googleapis.com/css2?family=Exo+2:wght@400;600;700&display=swap" rel="stylesheet">
<style>
  :root {
    --stage: #333333;
    --red: #d42a0c;
    --red-deep: #8c1407;
    --red-dark: #6e0f05;
    --ink: #3a3a3a;
    --grey: #555555;
    --rule: #bdbdbd;
    --paper: #ffffff;
    --white: #ffffff;
  }
  * { margin: 0; padding: 0; box-sizing: border-box; }
  html, body { width: 1200px; height: 866px; overflow: hidden; }
  body {
    background: var(--stage);
    font-family: "Exo 2", sans-serif;
    display: flex;
    align-items: center;
    justify-content: center;
    gap: 40px;
  }
  .card {
    position: relative;
    width: 540px;
    height: 309px;
    overflow: hidden;
    box-shadow: 0 12px 28px rgba(0,0,0,.45);
  }

  /* Front */
  .card--front {
    background: radial-gradient(ellipse at 20% 10%, #f1f1f1 0%, var(--paper) 55%);
    border-bottom: 9px solid var(--red);
  }
  .brand {
    position: absolute;
    top: 58px;
    right: 40px;
    display: flex;
    align-items: center;
    gap: 12px;
  }
  .brand__dot {
    width: 34px; height: 34px; border-radius: 50%;
    background: var(--red);
  }
  .brand__name {
    font-weight: 600;
    font-size: 30px;
    letter-spacing: 3px;
    color: var(--red-dark);
  }
  .contact {
    position: absolute;
    left: 36px;
    top: 130px;
  }
  .contact__name {
    font-weight: 700;
    font-size: 22px;
    color: var(--red);
    line-height: 1.05;
  }
  .contact__title {
    font-size: 14px;
    color: var(--ink);
    margin-bottom: 8px;
  }
  .contact__line {
    display: flex;
    align-items: center;
    gap: 7px;
    font-size: 14px;
    color: var(--ink);
    line-height: 1.5;
  }
  .contact__line svg { width: 14px; height: 14px; flex: none; }
  .rule {
    position: absolute;
    left: 230px;
    right: 36px;
    top: 212px;
    border-top: 1px solid var(--rule);
  }
  .web {
    position: absolute;
    right: 36px;
    bottom: 28px;
    font-size: 15px;
    color: var(--grey);
  }
  .web__domain { color: var(--red); }

  /* Back */
  .card--back {
    background: radial-gradient(ellipse at 25% 35%, #e02a0a 0%, #c41e08 40%, var(--red-deep) 100%);
  }
  .services {
    position: absolute;
    right: 46px;
    top: 50%;
    transform: translateY(-50%);
    display: grid;
    grid-template-columns: repeat(2, 96px);
    gap: 18px 26px;
  }
  .service {
    display: flex;
    flex-direction: column;
    align-items: center;
    gap: 6px;
    color: var(--white);
    font-size: 14px;
  }
  .service__icon {
    width: 66px; height: 54px;
    border: 2px solid var(--white);
    border-radius: 3px;
    display: flex; align-items: center; justify-content: center;
  }
  .service__icon svg { width: 40px; height: 34px; }
</style>
</head>
<body>

  <section class="card card--front" aria-label="Card front">
    <div class="brand">
      <span class="brand__dot"></span>
      <span class="brand__name">Halvick Design</span>
    </div>

    <div class="contact">
      <p class="contact__name">Myles Hartwell</p>
      <p class="contact__title">Managing Director</p>
      <p class="contact__line">
        <svg viewBox="0 0 16 16" aria-hidden="true"><rect x="1" y="1" width="14" height="14" rx="2" fill="none" stroke="#d42a0c" stroke-width="1.6"/><path d="M5 4c-1 1-1 3 1 5s4 2 5 1l-1.5-1.5-1 .8c-1-.4-2-1.4-2.3-2.3l.8-1z" fill="#d42a0c"/></svg>
        613-582-4179
      </p>
      <p class="contact__line">
        <svg viewBox="0 0 16 16" aria-hidden="true"><rect x="1" y="3" width="14" height="10" fill="#d42a0c"/><path d="M1 3l7 6 7-6" fill="none" stroke="#fff" stroke-width="1.4"/></svg>
        myles@halvickdesign.ca
      </p>
    </div>

    <div class="rule"></div>
    <p class="web">www.<span class="web__domain">halvickdesign</span>.ca</p>
  </section>

  <section class="card card--back" aria-label="Card back">
    <div class="services">
      <div class="service">
        <div class="service__icon">
          <svg viewBox="0 0 40 34" fill="none" stroke="#fff" stroke-width="2"><rect x="3" y="3" width="34" height="28"/><line x1="3" y1="10" x2="37" y2="10"/><rect x="14" y="18" width="12" height="8"/><line x1="20" y1="10" x2="20" y2="18"/></svg>
        </div>
        <span>3D Printer</span>
      </div>
      <div class="service">
        <div class="service__icon">
          <svg viewBox="0 0 40 34" fill="none" stroke="#fff" stroke-width="2"><rect x="10" y="3" width="20" height="6"/><line x1="20" y1="9" x2="20" y2="15"/><rect x="8" y="15" width="24" height="6"/><rect x="5" y="24" width="30" height="7"/></svg>
        </div>
        <span>Molding</span>
      </div>
      <div class="service">
        <div class="service__icon">
          <svg viewBox="0 0 40 34" fill="none" stroke="#fff" stroke-width="2"><path d="M8 5l10 6-3 4"/><path d="M15 15c0 4 2 6 2 6"/><path d="M10 25h22v5H10z"/><path d="M20 21c3 0 6 1 6 4"/></svg>
        </div>
        <span>Casting</span>
      </div>
      <div class="service">
        <div class="service__icon">
          <svg viewBox="0 0 40 34" fill="none" stroke="#fff" stroke-width="2"><rect x="3" y="3" width="34" height="22"/><line x1="20" y1="25" x2="20" y2="30"/><line x1="12" y1="31" x2="28" y2="31"/><path d="M20 8l6 3v6l-6 3-6-3v-6z"/></svg>
        </div>
        <span>3d Model</span>
      </div>
    </div>
  </section>

</body>
</html>
```